Business Card for Technology Startup

Design a 2-sided business card using the logo provided. We are a digital healthcare platform that provides a mobile app and web UI that helps caregivers, families, and doctors share information and provide better patient outcomes. We use AI and machine learning to help guide patients through their day-to-day life. The final design should communicate stability, peace, comfort, but also align with the image of an AI-driven technology startup.

I'd like the deliverable to by a Photoshop PSD file (with layers) that I can work with in pixlr.com. Should contain the following editable layers:
Name (ex. Karl Whitby)
Title (ex. Founder / CEO)
Email (ex. info@morventary.ai)
Phone (ex. (999) 482-7160)
Website (ex. https://morventary.ai)

```html
<!DOCTYPE html>
<html lang="en">
<head>
<meta charset="utf-8">
<title>Morventary Business Card</title>
<link rel="stylesheet" href="https://fonts.googleapis.com/css2?family=Montserrat:wght@400;500;700;800&display=swap">
<style>
  :root {
    --bg: #2b2b2d;
    --card-dark: #19191a;
    --card-dark-mark: #2c2c2e;
    --card-light: #ffffff;
    --ink: #111111;
    --accent: #1ea9e1;
    --accent-soft: #57c7ef;
  }
  * { margin: 0; padding: 0; box-sizing: border-box; }
  html, body {
    width: 1200px; height: 874px; overflow: hidden;
    background: var(--bg);
    font-family: "Montserrat", Arial, sans-serif;
  }
  .stage {
    width: 1200px; height: 874px;
    display: flex; flex-direction: column; align-items: center; justify-content: center;
    gap: 40px;
  }
  .card {
    width: 600px; height: 343px;
    border-radius: 22px;
    position: relative;
    box-shadow: 0 14px 30px rgba(0,0,0,.45);
  }
  .card--back { background: var(--card-dark); display: flex; align-items: center; justify-content: center; }
  .card--front { background: var(--card-light); }

  .wordmark { display: flex; align-items: center; gap: 18px; }
  .wordmark__dot { width: 34px; height: 34px; border-radius: 50%; }
  .wordmark__name { font-weight: 800; font-size: 62px; letter-spacing: -1px; line-height: 1; }
  .card--back .wordmark__dot { background: var(--card-dark-mark); }
  .card--back .wordmark__name { color: var(--card-dark-mark); }

  .card--front .wordmark { position: absolute; left: 70px; top: 86px; }
  .card--front .wordmark__dot { background: var(--accent); }
  .card--front .wordmark__name { color: var(--ink); }

  .identity {
    position: absolute; left: 150px; top: 232px; text-align: right; width: 140px;
  }
  .identity__name { color: var(--accent); font-weight: 700; font-size: 21px; line-height: 1.1; }
  .identity__title { color: var(--ink); font-weight: 400; font-size: 13.5px; margin-top: 3px; }

  .divider {
    position: absolute; left: 306px; top: 230px; width: 1px; height: 70px; background: var(--accent);
  }
  .contacts {
    position: absolute; left: 322px; top: 228px; list-style: none;
    font-size: 13.5px; color: var(--ink);
  }
  .contacts li { display: flex; align-items: center; gap: 9px; height: 24px; }
  .contacts svg { width: 13px; height: 13px; fill: var(--accent); flex: none; }
</style>
</head>
<body>
<main class="stage">
  <section class="card card--back" aria-label="Card back">
    <div class="wordmark">
      <span class="wordmark__dot"></span>
      <span class="wordmark__name">morventary</span>
    </div>
  </section>

  <section class="card card--front" aria-label="Card front">
    <div class="wordmark">
      <span class="wordmark__dot"></span>
      <span class="wordmark__name">morventary</span>
    </div>

    <div class="identity">
      <p class="identity__name">Karl Whitby</p>
      <p class="identity__title">Founder / CEO</p>
    </div>

    <span class="divider"></span>

    <ul class="contacts">
      <li>
        <svg viewBox="0 0 24 24" aria-hidden="true"><path d="M6.6 10.8a15.1 15.1 0 0 0 6.6 6.6l2.2-2.2a1 1 0 0 1 1-.25 11.4 11.4 0 0 0 3.6.57 1 1 0 0 1 1 1V20a1 1 0 0 1-1 1A17 17 0 0 1 3 4a1 1 0 0 1 1-1h3.5a1 1 0 0 1 1 1c0 1.25.2 2.45.57 3.57a1 1 0 0 1-.25 1z"/></svg>
        (999) 482-7160
      </li>
      <li>
        <svg viewBox="0 0 24 24" aria-hidden="true"><path d="M2 5h20v14H2z M2 5l10 8 10-8" fill="none" stroke="#1ea9e1" stroke-width="2.4"/></svg>
        info@morventary.ai
      </li>
      <li>
        <svg viewBox="0 0 24 24" aria-hidden="true"><circle cx="12" cy="12" r="10"/><path d="M2 12h20M12 2c3 3 3 17 0 20M12 2c-3 3-3 17 0 20" fill="none" stroke="#fff" stroke-width="1.4"/></svg>
        www.morventary.ai
      </li>
    </ul>
  </section>
</main>
</body>
</html>
```